Womans Supplement Designs

Launching a Supplement company and need to get some initial designs created, I've attached our logo and the bottle type that I want the samples done one.

This project is for our Whey Protein we are starting with Vanilla, chocolate and strawberry banana

(ALL DESIGN VARIATIONS MUST BE A WHITE BOTTLE NOT BLACK)

(FOR DESIGN SAMPLES PLEASE USE THE SUPPLEMENT BOTTLE STYLE I PROVIDED)

Whoever is selected the winner I will have more work for you to complete the disigns for the rest of the products in the line, Just want to get this shake completed first

Target Market(s)

Women

Requirements
Must have
• Must have our current logo involved

the name of this product will be "KIVA LUM"

Must have this slogan,

ALL-IN-ONE PREMIUM PROTEIN NUTRITIONAL SHAKE FOR BLACK WOMEN

This is our meal replacement

the design should try to keep the same look and feel of the existing provided supplement images

we are starting with chocolate, vanilla and strawberry banana

this is for women and should look colorful and appeal to them
Should not have
• Do not use an image of a person or lady, don't want it branded to a person

```html
<!DOCTYPE html>
<html lang="en">
<head>
<meta charset="utf-8">
<title>Kiva Lum – Vanilla Label</title>
<link href="https://fonts.googleapis.com/css2?family=Lato:wght@400;500&family=Orbitron:wght@500&display=swap" rel="stylesheet">
<style>
  :root {
    --backdrop: #ffb86b;
    --label-white: #ffffff;
    --accent: #e5a05c;
    --ink: #2b2b2b;
    --flavour-ink: #ffffff;
  }
  html, body {
    margin: 0;
    padding: 0;
    width: 940px;
    height: 1200px;
    overflow: hidden;
    background: var(--backdrop);
  }
  .canvas {
    position: relative;
    width: 940px;
    height: 1200px;
  }
  .label {
    position: absolute;
    left: 40px;
    top: 275px;
    width: 860px;
    height: 650px;
    background: var(--label-white);
    overflow: hidden;
  }
  .label__wave {
    position: absolute;
    inset: 0;
    width: 100%;
    height: 100%;
  }
  .label__wave path { fill: var(--accent); }

  .brand {
    position: absolute;
    top: 42px;
    left: 0;
    right: 0;
    display: flex;
    justify-content: center;
    align-items: center;
    gap: 14px;
  }
  .brand__square {
    width: 30px;
    height: 30px;
    background: var(--accent);
  }
  .brand__name {
    font-family: "Lato", sans-serif;
    font-weight: 500;
    font-size: 22px;
    letter-spacing: 4px;
    color: var(--ink);
  }

  .product-name {
    position: absolute;
    top: 176px;
    left: 0;
    right: 0;
    margin: 0;
    text-align: center;
    font-family: "Orbitron", sans-serif;
    font-weight: 500;
    font-size: 76px;
    letter-spacing: 6px;
    color: var(--accent);
    line-height: 1;
  }

  .tagline {
    position: absolute;
    top: 290px;
    left: 0;
    right: 0;
    margin: 0;
    text-align: center;
    font-family: "Lato", sans-serif;
    color: var(--ink);
    line-height: 1;
  }
  .tagline__small {
    display: block;
    font-size: 20px;
    font-weight: 400;
  }
  .tagline__large {
    display: block;
    font-size: 40px;
    font-weight: 400;
    margin: 6px 0 7px;
  }

  .flavour {
    position: absolute;
    left: 633px;
    top: 550px;
    font-family: "Orbitron", sans-serif;
    font-weight: 500;
    font-size: 30px;
    letter-spacing: 2px;
    color: var(--flavour-ink);
  }
</style>
</head>
<body>
<div class="canvas">
  <section class="label">
    <svg class="label__wave" viewBox="0 0 1005 760" preserveAspectRatio="none" aria-hidden="true">
      <path d="M1005,20 C960,260 860,420 700,470 C560,520 400,530 250,550 C100,570 20,600 0,680 L0,760 L1005,760 Z"/>
    </svg>

    <div class="brand">
      <span class="brand__square"></span>
      <span class="brand__name">AMARA GRACE</span>
    </div>

    <h1 class="product-name">KIVA LUM</h1>

    <p class="tagline">
      <span class="tagline__small">ALL-IN-ONE PREMIUM</span>
      <span class="tagline__large">PROTEIN NUTRITIONAL</span>
      <span class="tagline__small">SHAKE FOR BLACK WOMEN</span>
    </p>

    <div class="flavour">VANILLA</div>
  </section>
</div>
</body>
</html>
```